perforated vinyl window art

I am Franchise owner that needs to keep with the corporate image and logo requirements. The business is insurance and we are a store front office. I want to incorporate the following:
•The Brightfield Mutual (like harbor ridge) and my individual office name Lindqvist Harrow Insurance ltd.
•Chinese Version on Left door
•Modern looking
•Top of doors and same space on top of two windows needs to have Insurance Financial Services. I want the text to be a similar font to provided images.
•Mid part of the windows should be free of anything, so I can have more sunlight in my office. If part of a picture or letter was in the centre but originated in the bottom, that is fine, and maybe preferred.

Target Market(s)

our webpage is www.brightfieldmutual-example.ca under the about us, has logo's and usage there. The look and feel of the window art should look similar to this. Also, see attached pictures. The Lindqvist Harrow insurance in Gold is my prefered logo for my company under The Brightfield Mutual. The window picture is only for sizing and to give you a very rough idea. I have also included another design from a different office, I like the feel of this, but wantt to make it more specific to my office.

Industry/Entity Type

Insurance

Requirements
Must have
• •The Brightfield Mutual (like harbor ridge) and my individual office name Lindqvist Harrow Insurance ltd.
•Modern looking
- Should also include royalty free images, or paid for images.
- Include hours of operation - Monday to Friday 9am - 5pm
- Include address #274 23045-61 ave
- Phone number 555-302-9164

```html
<!DOCTYPE html>
<html lang="en">
<head>
<meta charset="utf-8">
<title>Lindqvist Harrow Insurance Ltd. – Window Graphics</title>
<link rel="stylesheet" href="https://fonts.googleapis.com/css2?family=Open+Sans:wght@600;700&family=Source+Sans+3:wght@400;600&display=swap">
<style>
  :root {
    --backdrop: #3a3533;
    --glass: #2c2a2a;
    --gold: #d3aa5c;
    --gold-panel: #c9a35e;
    --gold-tile: #c79d55;
    --gold-soft: #dcbf86;
    --ink: #2f2b28;
    --white: #ffffff;
  }
  * { box-sizing: border-box; margin: 0; padding: 0; }
  html, body { width: 1200px; height: 880px; overflow: hidden; }
  body {
    position: relative;
    background: var(--backdrop);
    font-family: "Open Sans", Arial, sans-serif;
  }
  .icon-library { position: absolute; width: 0; height: 0; }
  .icon-white { fill: var(--white); }
  .icon-cut { fill: var(--gold-tile); }
  .icon-line { fill: none; stroke: var(--gold-tile); stroke-width: 4; stroke-linejoin: round; }
  .icon-handle { fill: none; stroke: var(--white); stroke-width: 3; }

  .pane { position: absolute; background: var(--glass); }

  .headline {
    position: absolute; color: var(--gold);
    font-family: "Open Sans", Arial, sans-serif; font-weight: 700;
    font-size: 46px; line-height: 1; text-align: center;
  }
  .pane .headline { left: 0; right: 0; top: 14px; }

  /* Header band over doors */
  .header-band { left: 55px; top: 165px; width: 490px; height: 75px; }
  .leaf-ornament {
    position: absolute; left: 0; top: 0; width: 130px; height: 75px;
    background: linear-gradient(100deg, #c99d4e 0%, #a97f38 60%, var(--glass) 100%);
  }
  .header-band .headline { left: 140px; right: 0; }

  /* Door panels */
  .door-panel {
    position: absolute; top: 292px; height: 473px;
    background: var(--gold-panel); color: var(--ink); text-align: center;
  }
  .door-left { left: 88px; width: 189px; }
  .door-right { left: 330px; width: 188px; }
  .door-title { margin-top: 19px; font-size: 19px; font-weight: 700; }
  .unit-number {
    position: absolute; left: 56px; top: 0;
    font-size: 20px; font-weight: 700; color: rgba(255, 255, 255, 0.35);
  }
  .office-name {
    position: relative;
    display: flex; align-items: center; gap: 8px;
    margin: 22px 0 0 8px; height: 44px;
  }
  .office-name .dot { width: 30px; height: 30px; border-radius: 50%; background: var(--ink); flex: none; }
  .office-name span {
    font-size: 12.5px; font-weight: 600; line-height: 1.35; text-align: left;
    text-transform: uppercase; letter-spacing: 0.3px;
  }
  .door-phone { font-size: 19px; font-weight: 700; }
  .door-left .door-phone { margin-top: 44px; }
  .door-right .door-phone { margin-top: 27px; }
  .door-hours { margin-top: 17px; font-size: 16px; font-weight: 700; line-height: 1.1; }
  .door-hours small { display: block; font-size: 14px; font-weight: 600; }
  .advisor-photo {
    position: absolute; left: 0; right: 7px; bottom: 0; height: 295px;
    background: linear-gradient(180deg, #c4a76e 0%, #a88e66 35%, #2b2a2e 62%, #1f1f24 100%);
  }
  .coverage-collage { position: absolute; left: 0; bottom: 0; width: 188px; height: 290px; }

  /* Windows */
  .window-one { left: 565px; top: 168px; width: 270px; height: 515px; }
  .window-two { left: 853px; top: 168px; width: 288px; height: 508px; }

  .tagline {
    position: absolute; left: 0; top: 115px;
    color: var(--gold); text-align: left; white-space: nowrap;
    font-family: "Source Sans 3", Arial, sans-serif; font-weight: 400;
  }
  .window-two .tagline { top: 110px; }
  .tagline span { display: block; }
  .tagline .big { font-size: 44px; line-height: 44px; }
  .tagline .small { font-size: 29px; line-height: 30px; }
  .tagline .mid { font-size: 35px; line-height: 33px; }
  .window-one .big { margin-left: 35px; }
  .window-one .for { margin-left: 90px; }
  .window-one .mid { margin-left: 83px; }
  .window-one .things { margin-left: 56px; }
  .window-two .big { margin-left: 49px; }
  .window-two .for { margin-left: 104px; }
  .window-two .mid { margin-left: 97px; }
  .window-two .things { margin-left: 71px; }

  .coverage-tiles { position: absolute; left: 13px; bottom: 0; display: flex; gap: 5px; }
  .window-two .coverage-tiles { left: 19px; }
  .tile { position: relative; width: 79px; height: 196px; background: var(--gold-tile); }
  .tile-label {
    position: absolute; top: 6px; left: 50%;
    writing-mode: vertical-rl; transform: translateX(-50%) rotate(180deg);
    color: var(--white); font-family: "Source Sans 3", Arial, sans-serif;
    font-weight: 600; font-size: 19px; letter-spacing: 2px; line-height: 1;
  }
  .tile-icon { position: absolute; left: 5px; bottom: 8px; width: 69px; height: 60px; }
  .tile-figure {
    position: absolute; left: 10px; bottom: 8px; width: 58px; height: 70px;
    background: linear-gradient(180deg, #e6d2a8, #f3e8d2);
    border-radius: 6px 6px 0 0;
  }
</style>
</head>
<body>

  <svg class="icon-library" aria-hidden="true">
    <symbol id="icon-car" viewBox="0 0 70 55">
      <path class="icon-white" d="M14 22 L20 6 H50 L56 22 Z"/>
      <rect class="icon-white" x="2" y="20" width="66" height="22" rx="6"/>
      <rect class="icon-white" x="6" y="38" width="12" height="14" rx="2"/>
      <rect class="icon-white" x="52" y="38" width="12" height="14" rx="2"/>
      <path class="icon-cut" d="M19 20 L23 10 H47 L51 20 Z"/>
      <ellipse class="icon-cut" cx="12" cy="30" rx="5" ry="3"/>
      <ellipse class="icon-cut" cx="58" cy="30" rx="5" ry="3"/>
      <rect class="icon-cut" x="25" y="29" width="20" height="5" rx="1"/>
    </symbol>
    <symbol id="icon-house" viewBox="0 0 100 80">
      <rect class="icon-white" x="72" y="10" width="8" height="18"/>
      <polygon class="icon-white" points="2,40 50,4 98,40"/>
      <rect class="icon-white" x="12" y="38" width="76" height="42"/>
      <rect class="icon-cut" x="44" y="54" width="12" height="26"/>
      <rect class="icon-cut" x="20" y="48" width="14" height="12"/>
      <rect class="icon-cut" x="66" y="48" width="14" height="12"/>
    </symbol>
    <symbol id="icon-chart" viewBox="0 0 50 40">
      <rect class="icon-white" x="0" y="0" width="50" height="40"/>
      <polyline class="icon-line" points="6,34 18,20 26,27 40,10"/>
      <polygon class="icon-cut" points="34,6 46,3 44,15"/>
    </symbol>
    <symbol id="icon-briefcase" viewBox="0 0 60 42">
      <path class="icon-handle" d="M22 10 V3 H38 V10"/>
      <rect class="icon-white" x="0" y="10" width="60" height="32" rx="3"/>
      <rect class="icon-cut" x="0" y="20" width="60" height="2"/>
    </symbol>
    <symbol id="icon-plane" viewBox="0 0 60 50">
      <g transform="rotate(55 30 25)">
        <rect class="icon-white" x="27" y="0" width="6" height="50" rx="3"/>
        <polygon class="icon-white" points="30,16 2,30 2,35 30,27 58,35 58,30"/>
        <polygon class="icon-white" points="30,40 19,47 19,50 30,46 41,50 41,47"/>
      </g>
    </symbol>
  </svg>

  <div class="pane header-band">
    <div class="leaf-ornament" role="img" aria-label="Gold leafy tree branch ornament"></div>
    <div class="headline">Insurance</div>
  </div>

  <section class="door-panel door-left">
    <p class="door-title">Chinese Version</p>
    <p class="door-phone">555.302.9164</p>
    <p class="door-hours">Monday to Friday<small>9:00 am to 5:00 pm</small></p>
    <div class="advisor-photo" role="img" aria-label="Photo of a smiling insurance advisor in a dark business suit"></div>
  </section>

  <section class="door-panel door-right">
    <span class="unit-number">274</span>
    <div class="office-name">
      <i class="dot"></i>
      <span>Lindqvist Harrow<br>Insurance Ltd.</span>
    </div>
    <p class="door-phone">555.302.9164</p>
    <p class="door-hours">Monday to Friday<small>9:00 am to 5:00 pm</small></p>
    <svg class="coverage-collage" viewBox="0 0 188 290" role="img" aria-label="White icon collage of home, car, business, travel and investment coverage">
      <use href="#icon-chart" x="125" y="45" width="50" height="40"/>
      <use href="#icon-house" x="30" y="68" width="100" height="80"/>
      <use href="#icon-car" x="148" y="102" width="32" height="25"/>
      <use href="#icon-plane" x="143" y="133" width="48" height="40"/>
      <use href="#icon-car" x="65" y="185" width="70" height="55"/>
      <use href="#icon-house" x="140" y="193" width="45" height="36"/>
      <use href="#icon-briefcase" x="80" y="247" width="38" height="27"/>
      <use href="#icon-chart" x="130" y="250" width="30" height="24"/>
    </svg>
  </section>

  <section class="pane window-one">
    <div class="headline">Financial</div>
    <p class="tagline"><span class="big">Coverage</span><span class="small for">for the</span><span class="mid">important</span><span class="small things">things in life</span></p>
    <div class="coverage-tiles">
      <div class="tile"><span class="tile-label">AUTO</span><svg class="tile-icon" role="img" aria-label="Car icon"><use href="#icon-car"/></svg></div>
      <div class="tile"><span class="tile-label">HOME</span><svg class="tile-icon" role="img" aria-label="House icon"><use href="#icon-house"/></svg></div>
      <div class="tile"><span class="tile-label">BUSINESS</span><svg class="tile-icon" role="img" aria-label="Rising chart icon"><use href="#icon-chart"/></svg></div>
    </div>
  </section>

  <section class="pane window-two">
    <div class="headline">Services</div>
    <p class="tagline"><span class="big">Coverage</span><span class="small for">for the</span><span class="mid">important</span><span class="small things">things in life</span></p>
    <div class="coverage-tiles">
      <div class="tile"><span class="tile-label">LIFE</span><div class="tile-figure" role="img" aria-label="White silhouette of a parent walking with a child"></div></div>
      <div class="tile"><span class="tile-label">INVESTMENT</span><svg class="tile-icon" role="img" aria-label="Briefcase icon"><use href="#icon-briefcase"/></svg></div>
      <div class="tile"><span class="tile-label">TRAVEL</span><svg class="tile-icon" role="img" aria-label="Airplane icon"><use href="#icon-plane"/></svg></div>
    </div>
  </section>

</body>
</html>
```